Real estate Investment post card Design

I need a post card for Real Estate Marketing.

There are several similar cards on line.
Please see the post cards in this link to vidzorla
https://www.vidzorla.com/watch?v=pQmTr7W-b2Lx
At 1:18 the back of the card is very good.
For front of the card please refer to attached example gif.

Please also check the examples posted by me.

Everything needs to be the same except
1. Tomas Gets Homes
2. Phone number 287 914 5063
3. Website www.quillbrookestates.com
4. Email info@quillbrookestates.com
5. Picture needs to be replaced with my picture

The postcards need to be 2 sides and in color

Please let me know

Target Market(s)

Home owners who want to sell their houses for quick settlement and cash

Industry/Entity Type

Real Estate

Requirements
Must have
• I am copying this from another project as i think these instructions are valid for this project as well.
• Attention Designers - Special Requirements
• This project has special US Postcard Design requirements that apply to all submissions. The project is part of a print initiative, meaning that the selected design will be sent directly to print. If you have not, click download the templates below and ensure your design follows them before submitting.
• I plan to print the Post card by cardmillo in their Jumbo Format... copied below
• Document Trim Size
• 8.52" x 5.47"
• 216 x 139 mm
• 2556 x 1642 pixels
• Full Bleed Size
• Horizontal
• 8.64" x 5.59"
• 219 x 142 mm
• 2592 x 1677 pixels
• NOTE Please make sure you put return address on the post card
• 4725 7TH ST., PO Box. 5867
• NEW HYDE PARK, NY 11040
Nice to have
• Please see if you can add pictures that signify cash $$ and houses in the project. See the attached vidzorla.
Should not have
• Too much text on the first page

```html
<!DOCTYPE html>
<html lang="en">
<head>
<meta charset="utf-8">
<title>Tomas Gets Homes – Postcard</title>
<link rel="stylesheet" href="https://fonts.googleapis.com/css2?family=Roboto+Condensed:wght@400;700&family=Roboto:wght@500;700&family=Source+Sans+3:ital,wght@0,400;0,600;1,700&display=swap">
<style>
  :root {
    --navy: #1b3a63;
    --steel: #3d6291;
    --ink: #111111;
    --yellow: #f4e53a;
    --green: #1d8a3e;
    --panel: #f1f1f1;
    --page: #e9e7e4;
    --white: #ffffff;
  }
  * { box-sizing: border-box; margin: 0; padding: 0; }
  html, body { width: 997px; height: 1200px; overflow: hidden; }
  body { background: var(--page); position: relative; font-family: "Source Sans 3", sans-serif; color: var(--ink); }

  .card { position: absolute; background: var(--white); box-shadow: 0 3px 10px rgba(0,0,0,.25); overflow: hidden; }

  /* Front */
  .front { left: 63px; top: 54px; width: 774px; height: 501px; }
  .front-title { position: absolute; left: 31px; top: 14px; font-family: "Roboto Condensed", sans-serif; font-weight: 700; color: var(--navy); font-size: 58px; line-height: 1.1; white-space: nowrap; }
  .front-title .cash { display: block; font-size: 80px; line-height: 1.1; }
  .front-tagline { position: absolute; left: 31px; top: 200px; font-family: "Roboto Condensed", sans-serif; font-weight: 700; font-size: 40px; line-height: 1.13; color: var(--ink); }
  .front-cta { position: absolute; left: 31px; top: 348px; font-family: "Roboto Condensed", sans-serif; font-size: 27px; line-height: 1.2; color: var(--ink); }
  .front-phone { position: absolute; left: 31px; top: 410px; font-family: "Roboto Condensed", sans-serif; font-weight: 700; font-size: 37px; color: var(--ink); }
  .front-offer { position: absolute; left: 31px; top: 454px; font-family: "Roboto", sans-serif; font-weight: 700; font-size: 21px; color: var(--steel); }
  .front-art { position: absolute; left: 330px; top: 100px; width: 435px; height: 350px; background: radial-gradient(ellipse at 55% 45%, #4a5a70 0%, #8f9a92 45%, #d6d8cf 70%, rgba(255,255,255,0) 80%); }

  /* Back */
  .back { left: 159px; top: 628px; width: 775px; height: 502px; }
  .back-header { position: absolute; left: 0; top: 0; width: 100%; height: 81px; background: var(--navy); }
  .back-title { position: absolute; left: 23px; top: 20px; font-family: "Roboto", sans-serif; font-weight: 700; font-size: 33px; color: var(--yellow); letter-spacing: .5px; white-space: nowrap; }
  .back-pill { position: absolute; left: 438px; top: 22px; width: 318px; height: 38px; border-radius: 10px; background: var(--white); font-family: "Roboto Condensed", sans-serif; font-weight: 700; font-size: 22px; color: var(--ink); display: flex; align-items: center; justify-content: center; }
  .back-panel { position: absolute; left: 0; top: 81px; width: 455px; height: 353px; background: var(--panel); }
  .back-question { position: absolute; left: 23px; top: 8px; width: 430px; font-size: 19px; line-height: 23px; color: #222; }
  .back-question em { color: var(--green); font-weight: 700; }
  .back-rule { position: absolute; left: 23px; top: 62px; width: 423px; height: 2px; background: var(--ink); }
  .reasons { position: absolute; left: 23px; top: 80px; display: flex; }
  .reasons ul { list-style: none; width: 121px; font-size: 12.5px; line-height: 13.8px; color: #222; white-space: nowrap; }
  .agent-photo { position: absolute; left: 22px; top: 186px; width: 130px; height: 138px; background: linear-gradient(180deg, #e8e8e8 0%, #9a9a9a 60%, #2e2e2e 100%); }
  .agent-cta { position: absolute; left: 171px; top: 208px; font-family: "Roboto", sans-serif; font-weight: 500; font-size: 14px; line-height: 1.35; color: var(--ink); }
  .agent-offer { position: absolute; left: 171px; top: 247px; font-family: "Roboto", sans-serif; font-weight: 500; font-size: 14.5px; color: var(--steel); }
  .agent-phone { position: absolute; left: 171px; top: 266px; font-family: "Roboto Condensed", sans-serif; font-weight: 700; font-size: 27px; color: var(--navy); }
  .agent-links { position: absolute; left: 171px; top: 300px; font-family: "Roboto", sans-serif; font-weight: 700; font-size: 11px; line-height: 1.3; color: var(--ink); }
  .postage { position: absolute; left: 657px; top: 92px; width: 100px; height: 63px; border: 1.5px solid var(--ink); font-family: "Roboto", sans-serif; font-weight: 500; text-align: center; font-size: 9px; line-height: 1.45; padding-top: 5px; }
  .postage strong { font-size: 11px; display: block; line-height: 1.2; }
  .back-footer { position: absolute; left: 0; top: 443px; width: 100%; height: 59px; background: var(--navy); display: flex; align-items: center; justify-content: center; gap: 14px; }
  .back-footer .lead { font-family: "Roboto", sans-serif; font-weight: 500; font-size: 17px; color: var(--white); }
  .back-footer .offer { font-family: "Roboto", sans-serif; font-weight: 700; font-size: 21px; color: var(--yellow); }
</style>
</head>
<body>

<section class="card front">
  <h1 class="front-title">Tomas Gets Homes-<span class="cash">CA$H!</span></h1>
  <p class="front-tagline">Any Condition,<br>Any Situation</p>
  <div class="front-art" role="img" aria-label="Model house sitting on a pile of dollar bills"></div>
  <p class="front-cta">Call today for a FREE<br>private consultation</p>
  <p class="front-phone">287 914 5063</p>
  <p class="front-offer">Cash offer in 48 hours!</p>
</section>

<section class="card back">
  <header class="back-header">
    <h2 class="back-title">Tomas Gets Homes-CA$H</h2>
    <div class="back-pill">Any Condition, Any Situation</div>
  </header>

  <div class="back-panel">
    <p class="back-question">Do you need to sell your property quickly for any of the following reasons? <em>I can help!</em></p>
    <div class="back-rule"></div>
    <div class="reasons">
      <ul>
        <li>Dabe Relief</li><li>Loss of Job</li><li>Inherited House</li><li>Forced transfer</li><li>Failing Health</li><li>Death of Spouse</li>
      </ul>
      <ul>
        <li>Retirement</li><li>Tired Landlord</li><li>Out Grown House</li><li>Little or No Equitz</li><li>Bankruptcz</li><li>House too Large</li>
      </ul>
      <ul>
        <li>Costly Repairs Needed</li><li>Can't Afford Payment</li><li>Moving to New House</li><li>Divorce</li><li>Behind on Payments</li><li>Foreclosure</li>
      </ul>
    </div>
    <div class="agent-photo" role="img" aria-label="Portrait photo of the agent"></div>
    <p class="agent-cta">Call today for a FREE<br>private consultation</p>
    <p class="agent-offer">Cash offer in 48 hours!</p>
    <p class="agent-phone">287 914 5063</p>
    <p class="agent-links">www.quillbrookestates.com<br>info@quillbrookestates.com</p>
  </div>

  <div class="postage">STD U.S. POSTAGE<strong>PAID</strong>HARLOWE, FL<br>PERMIT NO. 47</div>

  <footer class="back-footer">
    <span class="lead">Call today for a FREEprivate consultation-</span>
    <span class="offer">CASH OFFER IN 48 HOURS!</span>
  </footer>
</section>

</body>
</html>
```